Skill Up Salary Up

Full Page
7.5 w x 10 h / 8 w x 10.75 h + .25" bleed
Full-Page Career Course Ad
Project Overview
• Goal: Create a visually attractive, modern, and uncluttered full-page magazine advertisement to list available career courses.
• Tone: Creative, professional, and attention-grabbing to prevent the reader from turning the page. The final design must prioritize readability.

Content Requirements
1. Header/Headline: Must be the primary focus. And grab peoples attention
2. Course Listing: A clear, well-organized list of the career courses.
________________________________________
Design & Aesthetic Directives
1. Layout & Readability (Crucial)
• The final ad must not look crowded or busy.
• Prioritize white space to make the text "breathe" and ensure the course list is easy to scan and read.
• Use a modern, clean, and professional typeface (font choice is critical for the aesthetic).
2. Visual Style
• Aim for a creative, modern, and fresh look. Avoid outdated or generic stock imagery/layouts.
3. Imagery/Graphic Element (Artist's Choice)
You have creative freedom regarding the main graphic element.
• Option A (Photography): Use a photo of a white male American with a collared shirt. The imagery should convey success, focus, or professional development.
• Option B (Vector/Illustration): Use a modern vector graphic, illustration, or abstract design. This could be used to symbolize growth, connection, or a career path.
The choice of graphic element is yours, but it must support the overall modern and uncrowded aesthetic.

Requirements
Must have
• Partial listing .. is part of the Harbor Lantern Course

```html
<!DOCTYPE html>
<html lang="en">
<head>
<meta charset="utf-8">
<title>Skill Up Salary Up – Upcoming Courses</title>
<link rel="stylesheet" href="https://fonts.googleapis.com/css2?family=Nunito:wght@600;700;800;900&family=Lato:wght@400;700;900&display=swap">
<style>
  :root{
    --canvas:#e6e5df;
    --paper:#ffffff;
    --paper-shade:#eceef1;
    --ink:#16161a;
    --orange:#f0901c;
    --orange-soft:#f8d3a4;
    --red:#e0242c;
    --red-soft:#ef8d92;
    --navy:#111a24;
    --navy-soft:#6c7580;
    --blue:#3d44b8;
    --blue-soft:#a9acde;
    --green:#1f9a76;
    --green-soft:#93ceb9;
    --purple:#62248c;
    --white:#ffffff;
  }
  *{box-sizing:border-box;margin:0;padding:0}
  html,body{width:1200px;height:1200px;overflow:hidden;background:var(--canvas)}
  body{font-family:"Nunito",sans-serif;color:var(--ink);position:relative}

  .ad-page{
    position:absolute;left:165px;top:20px;width:870px;height:1160px;
    background:linear-gradient(135deg,var(--paper) 45%,var(--paper-shade) 100%);
    box-shadow:0 6px 24px rgba(0,0,0,.12);overflow:hidden;
  }
  .course{position:absolute;padding-left:34px;border-left:2px solid var(--accent)}
  .course-tab{
    position:absolute;left:-2px;top:0;width:30px;height:30px;background:var(--accent);
  }
  .course-icon{
    position:absolute;left:16px;top:3px;width:26px;height:26px;border-radius:50%;
    background:var(--white);border:2px solid var(--accent);
  }
  .course-title{
    font-weight:900;font-size:20px;line-height:23px;color:var(--accent);
    text-transform:uppercase;padding-left:14px;padding-top:4px;letter-spacing:.2px;
  }
  .course-lede{font-weight:800;font-size:18px;line-height:22px;margin-top:6px}
  .course-label{font-weight:900;font-size:17px;margin-top:10px}
  .course-list{list-style:none;margin-top:4px}
  .course-list li{font-weight:600;font-size:16px;line-height:23px;position:relative;padding-left:14px}
  .course-list li::before{
    content:"";position:absolute;left:0;top:9px;width:6px;height:6px;border-radius:50%;background:var(--accent);
  }
  .course-date{
    display:inline-block;margin-top:10px;padding:3px 14px 2px;
    background:var(--accent);color:var(--white);font-weight:900;font-size:17px;
    box-shadow:0 5px 0 var(--accent-soft);
  }
  .course-divider{position:absolute;height:1px;background:var(--accent)}

  .is-orange{--accent:var(--orange);--accent-soft:var(--orange-soft)}
  .is-red{--accent:var(--red);--accent-soft:var(--red-soft)}
  .is-navy{--accent:var(--navy);--accent-soft:var(--navy-soft)}
  .is-blue{--accent:var(--blue);--accent-soft:var(--blue-soft)}
  .is-green{--accent:var(--green);--accent-soft:var(--green-soft)}

  .growth-illustration{
    position:absolute;left:215px;top:890px;width:250px;height:110px;
    background:linear-gradient(120deg,#ffffff 0%,#f6d7ae 45%,#8a55b0 100%);
  }
  .promo-band{
    position:absolute;left:0;bottom:0;width:100%;height:160px;background:var(--purple);
    color:var(--white);font-family:"Lato",sans-serif;text-align:center;padding-top:30px;
  }
  .promo-kicker{font-weight:700;font-size:26px;letter-spacing:.5px}
  .promo-headline{font-weight:900;font-size:44px;line-height:46px;letter-spacing:.5px}
  .promo-details{font-weight:400;font-size:20px;margin-top:6px;letter-spacing:.3px}
</style>
</head>
<body>
<main class="ad-page">

  <section class="course is-orange" style="left:60px;top:50px;width:370px;height:500px">
    <span class="course-tab"></span><span class="course-icon"></span>
    <h2 class="course-title">Harbor Lantern Course Business Skills &amp; Knowledge to:</h2>
    <p class="course-lede">Impress your interviewer<br>Maximize Income<br>Start / Run Your Business</p>
    <span class="course-date">4-5 MONTHS NOV 2025</span>
    <p class="course-label">PARTIAL LISTING:</p>
    <ul class="course-list">
      <li>Computers.</li><li>Investments.</li><li>Finance.</li><li>Business Strategy.</li>
      <li>Real Estate.</li><li>Communication.</li><li>Sales.</li><li>Healthcare.</li>
      <li>Marketing.</li><li>Accounting.</li><li>LedgerPal.</li>
    </ul>
  </section>
  <div class="course-divider is-orange" style="left:94px;top:572px;width:320px"></div>

  <section class="course is-red" style="left:60px;top:590px;width:370px;height:400px">
    <span class="course-tab"></span><span class="course-icon"></span>
    <h2 class="course-title">Software, Web &amp; Apps:</h2>
    <p class="course-lede"># 2 Best Tech Job<br>Civic Ledger Report 2025</p>
    <p class="course-label">Job Opportunities:</p>
    <ul class="course-list">
      <li>Computer Programmer.</li><li>Software Developer/Mobile.</li><li>Engineer / Developer (Apps).</li>
    </ul>
    <p class="course-label">Optional:</p>
    <ul class="course-list"><li style="font-size:18px">Bachelors in Prog.&amp; Tech.</li></ul>
    <span class="course-date">NOV 2025</span>
  </section>

  <div class="growth-illustration" role="img" aria-label="Illustration of a businessman climbing purple stairs beside a rising orange arrow"></div>

  <section class="course is-navy" style="left:470px;top:70px;width:360px;height:260px">
    <span class="course-tab"></span><span class="course-icon"></span>
    <h2 class="course-title">Bookkeeping LedgerPal:</h2>
    <p class="course-lede">Train for a quality job<br>Manage your own books</p>
    <ul class="course-list" style="margin-top:10px">
      <li>Finance Management.</li><li>Customer &amp; Vendor Mgmt.</li><li>Advanced Tools.</li>
    </ul>
    <span class="course-date">5 WEEKS NOV 2025</span>
  </section>
  <div class="course-divider is-navy" style="left:504px;top:350px;width:310px;opacity:.5"></div>

  <section class="course is-blue" style="left:470px;top:370px;width:360px;height:320px">
    <span class="course-tab"></span><span class="course-icon"></span>
    <h2 class="course-title">IT Desktop &amp;<br>Networking Support:</h2>
    <p class="course-lede">#2 Best Job<br>Civic Ledger Report 2025</p>
    <p class="course-label">Masters IT:</p>
    <ul class="course-list">
      <li>Desktop OS.</li><li>Networks.</li><li>Servers.</li><li>Cloud.</li>
    </ul>
    <span class="course-date">7 MONTHS DEC 2025</span>
  </section>
  <div class="course-divider is-blue" style="left:504px;top:708px;width:310px"></div>

  <section class="course is-green" style="left:470px;top:725px;width:360px;height:275px">
    <span class="course-tab"></span><span class="course-icon"></span>
    <h2 class="course-title">DeskSuite Office-<br>Computers</h2>
    <p class="course-lede">The New Job Prerequisite</p>
    <ul class="course-list" style="margin-top:8px">
      <li>Spreadsheets.</li><li>Documents.</li><li>Email &amp; Calendar.</li><li>Slides.</li>
    </ul>
    <p class="course-label" style="margin-top:6px">Computer lab available to practice</p>
    <span class="course-date">5 WEEKS DEC 2025</span>
  </section>

  <footer class="promo-band">
    <p class="promo-kicker">SKILL UP SALARY UP</p>
    <h1 class="promo-headline">UPCOMING COURSES</h1>
    <p class="promo-details">MEN &amp; WOMEN | IN-PERSON &amp; ONLINE | PARTIAL SCHOLARSHIPS</p>
  </footer>
</main>
</body>
</html>
```